Tallow Crest Business Card

We need a business card designed for a a company called "Tallow Crest". We offer consulting, coaching and training to business leaders and coaches (across the world) using the latest findings in neuroscience, social and emotional intelligence and positive psychology. The final design should communicate the use of brain science to create sustainable relationships.

The card should be doublesided. The logo is attached and names and titles will be provided to the successful designer. Thank you.

Industry/Entity Type

Training

```html
<!DOCTYPE html>
<html lang="en">
<head>
<meta charset="utf-8">
<title>Tallow Crest Business Card</title>
<link rel="stylesheet" href="https://fonts.googleapis.com/css2?family=Ubuntu:wght@400;500;700&display=swap">
<style>
  :root {
    --backdrop: #e6e6e6;
    --card-white: #ffffff;
    --charcoal: #353832;
    --brand-blue: #0a80c4;
    --brand-lime: #b8d20f;
    --text-dark: #2b2b2b;
    --text-light: #ffffff;
  }
  * { box-sizing: border-box; margin: 0; padding: 0; }
  html, body {
    width: 1200px; height: 861px; overflow: hidden;
    background: var(--backdrop);
    font-family: "Ubuntu", sans-serif;
  }
  .canvas { position: relative; width: 1200px; height: 861px; }
  .card {
    position: absolute; top: 265px;
    width: 500px; height: 330px;
    box-shadow: 0 6px 18px rgba(0,0,0,0.18);
  }
  .card--front { left: 90px; background: var(--card-white); }
  .card--back  {
    left: 620px; background: var(--charcoal);
    display: flex; justify-content: center; align-items: center;
  }

  .wordmark {
    display: flex; align-items: center; gap: 10px;
    font-weight: 700; color: var(--brand-blue);
    letter-spacing: 0.5px; line-height: 1; white-space: nowrap;
  }
  .wordmark__square { background: var(--brand-lime); flex: none; }
  .card--front .wordmark { position: absolute; left: 36px; top: 58px; font-size: 30px; }
  .card--front .wordmark__square { width: 26px; height: 26px; }
  .card--back .wordmark { font-size: 38px; }
  .card--back .wordmark__square { width: 32px; height: 32px; }

  .identity {
    position: absolute; right: 26px; top: 112px;
    display: flex; flex-direction: column; align-items: flex-end; gap: 10px;
  }
  .identity__name {
    background: var(--charcoal); color: var(--text-light);
    font-weight: 500; font-size: 19px; line-height: 1.2; padding: 3px 8px;
  }
  .identity__title {
    background: var(--brand-blue); color: var(--text-light);
    font-size: 11px; line-height: 1.3; padding: 3px 8px; letter-spacing: 0.3px;
  }

  .address {
    position: absolute; left: 0; right: 0; top: 214px;
    display: flex; justify-content: center; align-items: center; gap: 8px;
    font-size: 12.5px; line-height: 16px; font-weight: 500; color: var(--text-dark);
    white-space: nowrap;
  }

  .contact-band {
    position: absolute; left: 30px; right: 26px; bottom: 24px; height: 66px;
    background: var(--charcoal); color: var(--text-light);
    display: flex; justify-content: space-between; align-items: center;
    padding: 0 12px;
  }
  .contact-band ul { list-style: none; display: flex; flex-direction: column; gap: 10px; }
  .contact-band li { display: flex; align-items: center; gap: 8px; line-height: 1.2; white-space: nowrap; }
  .contact-band__phones { font-size: 14px; }
  .contact-band__online { font-size: 11px; align-items: flex-end; }
  .icon { width: 13px; height: 13px; flex: none; }
</style>
</head>
<body>
<main class="canvas">

  <section class="card card--front" aria-label="Card front">
    <div class="wordmark"><span class="wordmark__square"></span>Tallow Crest</div>

    <div class="identity">
      <div class="identity__name">JOHN DOE</div>
      <div class="identity__title">POSITION HELD</div>
    </div>

    <p class="address">
      <svg class="icon" viewBox="0 0 12 14" aria-hidden="true">
        <rect x="1" y="1" width="10" height="13" fill="var(--brand-lime)"/>
        <rect x="3" y="3" width="2" height="2" fill="#fff"/><rect x="7" y="3" width="2" height="2" fill="#fff"/>
        <rect x="3" y="7" width="2" height="2" fill="#fff"/><rect x="7" y="7" width="2" height="2" fill="#fff"/>
      </svg>
      #123 Lorem Ipsum Street, Dolor City, 19017
    </p>

    <div class="contact-band">
      <ul class="contact-band__phones">
        <li>
          <svg class="icon" viewBox="0 0 14 14" aria-hidden="true">
            <path d="M2 12 L12 2 L13 4 L4 13 Z M1 10 L4 13 L2 13 Z" fill="var(--brand-lime)"/>
          </svg>123.456.7890
        </li>
        <li>
          <svg class="icon" viewBox="0 0 14 14" aria-hidden="true">
            <rect x="4" y="1" width="7" height="12" rx="1" fill="var(--brand-lime)"/>
            <rect x="5.5" y="3" width="4" height="3" fill="var(--charcoal)"/>
          </svg>123.456.7890
        </li>
      </ul>
      <ul class="contact-band__online">
        <li>name@tallowcrest.com
          <svg class="icon" viewBox="0 0 14 14" aria-hidden="true">
            <rect x="1" y="3" width="12" height="8" fill="var(--brand-lime)"/>
            <path d="M1 3 L7 8 L13 3" stroke="var(--charcoal)" fill="none"/>
          </svg>
        </li>
        <li>www.tallowcrest.com
          <svg class="icon" viewBox="0 0 14 14" aria-hidden="true">
            <rect x="1" y="2" width="12" height="8" fill="none" stroke="var(--brand-lime)" stroke-width="1.5"/>
            <rect x="4" y="11" width="6" height="1.5" fill="var(--brand-lime)"/>
          </svg>
        </li>
      </ul>
    </div>
  </section>

  <section class="card card--back" aria-label="Card back">
    <div class="wordmark"><span class="wordmark__square"></span>Tallow Crest</div>
  </section>

</main>
</body>
</html>
```